2019 Camp Brindlecove Golf Tournament

I am looking for someone to design a flyer for our golf benefit tournament. We are a Christian camp that uses this money to help provide scholarships and improve our facilities. The flyer will need to be 8.5 x 11 inches. One side will the information and registrations page. I have included a word document that has all the information. I have also included last years flyer in case that helps. We are looking for a new design, this one has been used for several years. The other side of the flyer will be used for mailing. it will need to be folded for mailing purposes. Please be sure to design half the back side as instructed, the post office is very strict about this mail out.

Target Market(s)

Golfers and potential businesses as donors

Colors

Designer to choose colors to be used in the design.

Requirements
Must have
• Golf theme, all the information provided in word document

```html
<!DOCTYPE html>
<html lang="en">
<head>
<meta charset="utf-8">
<title>Camp Brindlecove Golf Benefit Tournament Mailer</title>
<link href="https://fonts.googleapis.com/css2?family=Montserrat:wght@600;800&family=Oswald:wght@500;600&family=Roboto:wght@400;500&display=swap" rel="stylesheet">
<style>
  :root {
    --backdrop: #e4e4e4;
    --paper: #f7f7f7;
    --ink: #333333;
    --forest: #1f4d2a;
    --grass-dark: #1c7028;
    --grass-mid: #2f9a3a;
    --grass-light: #5cbc4c;
    --lime: #d4ec3a;
    --white: #ffffff;
  }
  * { box-sizing: border-box; margin: 0; padding: 0; }
  html, body { width: 1200px; height: 900px; overflow: hidden; background: var(--backdrop); }
  .sheet {
    position: absolute; left: 50px; top: 25px; width: 1100px; height: 850px;
    display: flex; box-shadow: 0 4px 18px rgba(0,0,0,.12);
  }
  .panel { position: relative; width: 550px; height: 850px; overflow: hidden; }

  /* Mailing side */
  .mailing { background: var(--paper); }
  .mailing-layout {
    position: absolute; width: 850px; height: 550px;
    left: -150px; top: 150px; transform: rotate(90deg);
  }
  .return-box {
    position: absolute; left: 30px; top: 30px; width: 420px; height: 490px;
    border: 2px solid var(--forest);
  }
  .return-name {
    position: absolute; left: 24px; top: 22px;
    font-family: "Montserrat", sans-serif; font-weight: 800; font-size: 17px;
    color: var(--forest); letter-spacing: .5px; line-height: 1.3;
  }
  .return-address {
    position: absolute; left: 24px; top: 112px;
    font-family: "Roboto", sans-serif; font-size: 12px; color: var(--ink); line-height: 1.5;
  }
  .return-address .pin { display: inline-block; vertical-align: -2px; margin-right: 4px; }
  .permit {
    position: absolute; right: 40px; top: 30px; width: 96px; height: 88px;
    border: 1.5px solid var(--ink); padding: 8px 6px;
    font-family: "Roboto", sans-serif; font-size: 10.5px; color: var(--ink);
    text-align: center; line-height: 1.4;
  }
  .address-lines { position: absolute; left: 510px; top: 250px; width: 250px; }
  .address-lines span { display: block; height: 1px; background: #777; margin-bottom: 36px; }

  /* Cover side */
  .cover { background: var(--grass-mid); }
  .cover-photo {
    position: absolute; inset: 0;
    background:
      radial-gradient(circle at 50% 64%, rgba(230,245,238,.55) 0, rgba(120,200,110,.35) 18%, rgba(0,0,0,0) 32%),
      radial-gradient(ellipse at 50% 65%, var(--grass-light), var(--grass-mid) 45%, var(--grass-dark));
  }
  .frame { position: absolute; inset: 30px; border: 3px solid var(--white); }
  .title-badge {
    position: absolute; left: 130px; top: 70px; width: 290px; text-align: center;
    font-family: "Montserrat", sans-serif; font-weight: 800; color: var(--white);
  }
  .title-golf { font-size: 30px; line-height: 1; }
  .title-benefit {
    display: block; font-family: "Oswald", sans-serif; font-weight: 500;
    font-size: 26px; color: var(--lime); letter-spacing: 4px;
    border-top: 2px solid var(--lime); border-left: 2px solid var(--lime); border-right: 2px solid var(--lime);
    margin: 4px 20px 0; line-height: 1.2;
  }
  .title-tournament {
    display: block; background: var(--lime); color: var(--forest);
    font-size: 24px; margin: 0 20px; padding: 4px 0;
  }
  .event-date {
    position: absolute; left: 0; right: 0; top: 230px; text-align: center;
    font-family: "Oswald", sans-serif; font-weight: 600; font-size: 40px; color: var(--white);
  }
  .event-date sup { font-size: 20px; }
  .camp-arc { position: absolute; left: 0; top: 300px; width: 550px; height: 400px; }
  .camp-arc text {
    font-family: "Montserrat", sans-serif; font-weight: 800; font-size: 40px;
    fill: var(--white); letter-spacing: 2px;
  }
</style>
</head>
<body>
  <main class="sheet">
    <section class="panel mailing">
      <div class="mailing-layout">
        <div class="return-box">
          <div class="return-name">CAMP BRINDLECOVE<br>GOLF BENEFIT TOURNAMENT</div>
          <div class="return-address">
            <svg class="pin" width="10" height="14" viewBox="0 0 10 14"><path d="M5 0C2.2 0 0 2.2 0 5c0 3.6 5 9 5 9s5-5.4 5-9c0-2.8-2.2-5-5-5zm0 7a2 2 0 110-4 2 2 0 010 4z" fill="#333"/></svg>PO Box 4410<br>Marlow, AR 72999
          </div>
        </div>
        <div class="permit">Non Profit Org<br>U.S. postage<br>PAID<br>Marlow AR<br>Permit#7</div>
        <div class="address-lines"><span></span><span></span><span></span><span></span></div>
      </div>
    </section>

    <section class="panel cover">
      <div class="cover-photo" role="img" aria-label="Photograph of green golf course grass with a white golf ball sitting in the cup"></div>
      <div class="frame"></div>
      <div class="title-badge">
        <div class="title-golf">GOLF</div>
        <span class="title-benefit">BENEFIT</span>
        <span class="title-tournament">TOURNAMENT</span>
      </div>
      <div class="event-date">5<sup>th</sup> april 2019</div>
      <svg class="camp-arc" viewBox="0 0 550 400">
        <defs><path id="arc" d="M110 250 A170 170 0 0 1 450 230"/></defs>
        <text><textPath href="#arc" startOffset="50%" text-anchor="middle">CAMP BRINDLECOVE</textPath></text>
      </svg>
    </section>
  </main>
</body>
</html>
```